Redesign current business card for food company

i would like to redesign my business card. our company is food company, our product range from chips, juices, milk and etc (mostly dried food stuff).
I want o keep same logo but , the rest is open to new design.
you can check at our website about our company www.velqorafare.com

Target Market(s)

most of food company

Industry/Entity Type

Business

Contact Information for Business Card

I want to keep more to blue color...

Colors
3176b5
abd036

Requirements
Must have
• our old logo
Nice to have
• we do not mind to have nice material on bus card in order to accomplish nice design. for example: using spot uv, embossed and etc.

```html
<!DOCTYPE html>
<html lang="en">
<head>
<meta charset="utf-8">
<title>Velqora Business Card</title>
<link rel="stylesheet" href="https://fonts.googleapis.com/css2?family=Source+Sans+3:wght@400;600;700&display=swap">
<style>
  :root {
    --stage: #000000;
    --blue-light: #18a3e2;
    --blue-mid: #1d7fc4;
    --blue-deep: #1c4f95;
    --orange: #f7931e;
    --yellow: #fde31c;
    --amber: #f9b418;
    --logo-blue: #1e6fb8;
    --white: #ffffff;
  }
  * { margin: 0; padding: 0; box-sizing: border-box; }
  html, body {
    width: 1200px; height: 900px; overflow: hidden;
    background: var(--stage);
    font-family: "Source Sans 3", "Myriad Pro", sans-serif;
  }
  .card {
    position: absolute; top: 275px; width: 477px; height: 293px; overflow: hidden;
  }
  .card-front {
    left: 116px;
    border-radius: 0 55px 0 55px;
    background: linear-gradient(180deg, var(--blue-light) 0%, var(--blue-mid) 45%, var(--blue-deep) 100%);
  }
  .card-back {
    left: 622px;
    border-radius: 55px 0 55px 0;
    background: linear-gradient(135deg, var(--amber) 0%, var(--yellow) 55%, var(--orange) 100%);
  }
  .card-curves { position: absolute; inset: 0; width: 100%; height: 100%; }
  .brand-name {
    position: absolute; font-weight: 700; letter-spacing: -0.5px; line-height: 1;
  }
  .card-front .brand-name { left: 40px; top: 32px; font-size: 54px; color: var(--white); }
  .card-back .brand-name {
    left: 0; right: 0; top: 112px; text-align: center; font-size: 76px; color: var(--logo-blue);
  }
  .contact-block { position: absolute; left: 37px; top: 110px; color: var(--white); }
  .person-name { font-size: 18px; font-weight: 700; line-height: 1.1; }
  .person-title { font-size: 13px; line-height: 1.3; }
  .company-name { font-size: 14.5px; font-weight: 600; margin-top: 11px; line-height: 1.2; }
  .company-address { font-size: 13px; margin-top: 4px; line-height: 1.3; }
  .contact-list { list-style: none; margin-top: 8px; }
  .contact-list li {
    display: flex; align-items: center; gap: 6px; font-size: 13px; line-height: 17.5px;
  }
  .contact-list svg { width: 10px; height: 10px; fill: var(--white); flex: none; }
</style>
</head>
<body>

<section class="card card-front">
  <svg class="card-curves" viewBox="0 0 477 293" preserveAspectRatio="none" aria-hidden="true">
    <defs>
      <linearGradient id="curveTop" x1="0" y1="0" x2="0" y2="1">
        <stop offset="0" stop-color="#1b8fd4"/>
        <stop offset="1" stop-color="#1c4f95"/>
      </linearGradient>
      <linearGradient id="curveBottom" x1="0" y1="0" x2="0" y2="1">
        <stop offset="0" stop-color="#1c4f95"/>
        <stop offset="1" stop-color="#1aa0e0"/>
      </linearGradient>
    </defs>
    <path d="M245 0 C255 80 320 140 385 148 C430 150 460 160 477 170 L477 0 Z" fill="url(#curveTop)" opacity="0.75"/>
    <path d="M205 293 C225 200 300 150 385 148 C430 148 460 140 477 128 L477 293 Z" fill="url(#curveBottom)" opacity="0.8"/>
  </svg>

  <div class="brand-name">Velqora</div>

  <div class="contact-block">
    <p class="person-name">Darren Holloway</p>
    <p class="person-title">President</p>
    <p class="company-name">Velqora Enterprises Corp.</p>
    <p class="company-address">2750 Marlow Ridge Ave. Fairbend, CA 90412</p>
    <ul class="contact-list">
      <li><svg viewBox="0 0 10 10"><path d="M2 0.5 L3.6 2.6 L2.8 3.6 C3.4 5 5 6.6 6.4 7.2 L7.4 6.4 L9.5 8 L8.4 9.5 C4.5 9.2 0.8 5.5 0.5 1.6 Z"/></svg>555 014 2231</li>
      <li><svg viewBox="0 0 10 10"><path d="M2.5 0.5 H7 V3 H9.5 V9.5 H0.5 V3 H2.5 Z M3.5 1.5 V3 H6 V1.5 Z M2 5 V6 H3 V5 Z M4.5 5 V6 H5.5 V5 Z M7 5 V6 H8 V5 Z M2 7 V8 H3 V7 Z M4.5 7 V8 H5.5 V7 Z M7 7 V8 H8 V7 Z"/></svg>555 014 2239</li>
      <li><svg viewBox="0 0 10 10"><path d="M2.5 0 H7.5 A0.8 0.8 0 0 1 8.3 0.8 V9.2 A0.8 0.8 0 0 1 7.5 10 H2.5 A0.8 0.8 0 0 1 1.7 9.2 V0.8 A0.8 0.8 0 0 1 2.5 0 Z M2.8 1.2 V7.6 H7.2 V1.2 Z M5 8.2 A0.6 0.6 0 1 0 5 9.4 A0.6 0.6 0 1 0 5 8.2 Z"/></svg>555 018 4470</li>
      <li><svg viewBox="0 0 10 10"><path d="M0.5 2 H9.5 V8.5 H0.5 Z M1.2 2.6 L5 5.6 L8.8 2.6 Z"/></svg>Darren@velqorafare.com</li>
    </ul>
  </div>
</section>

<section class="card card-back">
  <svg class="card-curves" viewBox="0 0 477 293" preserveAspectRatio="none" aria-hidden="true">
    <path d="M0 150 C60 140 170 140 250 180 C290 210 310 260 318 293 L0 293 Z" fill="#f9a21b" opacity="0.55"/>
    <path d="M10 120 C40 40 120 0 240 0 L0 0 Z" fill="#f8a81a" opacity="0.45"/>
    <path d="M130 0 C220 30 280 110 290 200 L477 200 L477 0 Z" fill="#fde21c" opacity="0.35"/>
  </svg>
  <div class="brand-name">Velqora</div>
</section>

</body>
</html>
```